Keystone Ridge Construction LLC

We need a professional and colorful website that describes our company [please see below]:

CORE COMPETENCIES

About Us: Keystone Ridge Construction, LLC is a veteran-owned business, and is a leading force in the construction industry. We have continuously provided exceptional services to our clients. With a wealth of experience and a commitment of excellence, we have earned a reputation for delivering high-quality projects on time and within budget.

Core Competencies:

Experience: With decades of experience, we bring unparalleled expertise to every project we undertake. Our team consists of seasoned professionals who are experts in their respective fields.

Portfolio: Our portfolio encompasses a wide range of construction projects, including commercial building, industrial facilities, infrastructure development and more.

Keystone Ridge: We stay at the forefront of industry trends and technologies, leveraging the latest tools and techniques to deliver innovative solutions.

Client Satisfaction: Our commitment to client satisfaction is unwavering. We prioritize open communication, transparency, and responsiveness, working closely with clients to understand their needs and deliver results.

Safety: Safety is our top priority on every job site. We adhere to the highest safety standards and implement rigorous safety protocols to ensure the well-being of our workers and stakeholders.

KEY SERVICES

General Contracting
Construction Management
Design-Build Services
Pre-construction Planning
Value Engineering
Sustainable Construction Practices
Renovation and Remodeling
Quality Assurance and Control
Project Estimating and Budgeting
Permitting and Regulatory Compliance

CONTACT INFORMATION

Douglas Whitfield, President
Email Address [TBD]
Website Address [TBD]
555.214.6093

Federal Government and Commercial Agencies

Construction and Design Build

• Please use our attached logo and color scheme that was designed through Pixel Forum. Please include the Nation's Capitol building with a patriotic feel and include a diverse work force. Include federal buildings in the pictures. Please include in the opeing tagline that the company is Veteran Owned.

```html
<!DOCTYPE html>
<html lang="en">
<head>
<meta charset="utf-8">
<title>Keystone Ridge Construction, LLC</title>
<link href="https://fonts.googleapis.com/css2?family=Cinzel:wght@500;600;700&family=Montserrat:wght@400;500;600;700&display=swap" rel="stylesheet">
<style>
:root{
  --navy:#24306e;
  --navy-deep:#1d275e;
  --green:#8dc63f;
  --green-dark:#76ad2c;
  --ink:#2b2b2b;
  --muted:#6b6f80;
  --paper:#ffffff;
  --mist:#eceff6;
  --line:#c9cde0;
}
*{box-sizing:border-box;margin:0;padding:0}
html,body{width:1200px;height:4515px;overflow:hidden}
body{position:relative;background:var(--paper);font-family:"Montserrat",sans-serif;color:var(--ink)}
.abs{position:absolute}
.eyebrow{color:var(--green);font-size:18px;font-weight:500;letter-spacing:.5px}
.heading{font-family:"Cinzel",serif;font-weight:600;color:var(--navy);font-size:39px;line-height:44px;letter-spacing:1.5px}
.rule{width:70px;height:4px;background:var(--green)}

/* top bar */
.topbar-green{left:552px;top:0;width:330px;height:40px;background:var(--green);clip-path:polygon(0 0,100% 0,93% 100%,7% 100%)}
.topbar-navy{left:858px;top:0;width:342px;height:40px;background:var(--navy)}
.topbar-text{color:#fff;font-size:13px;font-weight:500;display:flex;align-items:center;gap:10px;top:11px;white-space:nowrap}
.topbar-icon{width:20px;height:20px;border-radius:50%;background:#fff;display:flex;align-items:center;justify-content:center}

/* hero */
.hero{left:0;top:0;width:1200px;height:762px;background:linear-gradient(180deg,#ffffff 0%,#f4f8fc 18%,#c9def0 45%,#9fc3e4 70%,#e6eef6 100%);clip-path:polygon(0 0,100% 0,100% 600px,50% 745px,0 600px)}
.hero-band{left:0;top:560px;width:1200px;height:210px}
.logo{left:110px;top:20px;width:230px;text-align:center;color:var(--navy);font-family:"Cinzel",serif;font-weight:600;white-space:nowrap}
.logo-mark{width:22px;height:22px;background:var(--green);margin:0 auto 8px}
.logo-name{font-size:22px;letter-spacing:1px;line-height:26px}
.logo-sub{font-size:9px;letter-spacing:1.2px;margin-top:4px}
.nav{top:80px;left:0;width:1200px;font-size:13px;font-weight:500;color:var(--navy);letter-spacing:.5px}
.nav a{position:absolute;color:var(--navy);text-decoration:none;white-space:nowrap}
.nav .sep{position:absolute;top:2px;width:1px;height:14px;background:#b7bccc}
.nav .active::after{content:"";position:absolute;left:0;right:0;bottom:-10px;height:3px;background:var(--green)}
.hero-tag{left:453px;top:177px;width:296px;height:30px;background:var(--green);color:#fff;font-size:13px;font-weight:500;display:flex;align-items:center;justify-content:center}
.hero-title{left:0;top:218px;width:1200px;text-align:center;font-family:"Cinzel",serif;font-weight:600;color:var(--navy);font-size:47px;line-height:45px;letter-spacing:3px}
.btn-navy{left:524px;top:324px;width:164px;height:44px;background:var(--navy);color:#fff;font-size:13px;font-weight:600;display:flex;align-items:center;justify-content:center;letter-spacing:.5px}
.hero-arrow{top:312px}

/* about */
.about-frame{left:84px;top:955px;width:473px;height:317px;background:var(--navy)}
.about-green-left{left:84px;top:1030px;width:22px;height:222px;background:var(--green)}
.about-green-right{left:536px;top:955px;width:21px;height:270px;background:var(--green)}
.about-photo{left:105px;top:851px;width:431px;height:400px;background:linear-gradient(160deg,#dfe7ee 0%,#f2f2ef 45%,#c8cfc6 75%,#6f8a4f 100%)}
.about-copy{left:620px;top:851px;width:520px}
.about-copy .heading{font-size:34px;line-height:44px;letter-spacing:1px;white-space:nowrap}
.about-copy p{font-size:18px;line-height:27px;color:#2f2f2f;margin-top:24px;width:510px}
.btn-green{width:190px;height:46px;background:var(--green);color:#fff;font-size:15px;font-weight:600;display:flex;align-items:center;justify-content:center;letter-spacing:.5px}

/* core */
.core{left:0;top:1354px;width:1200px;height:802px;background:linear-gradient(180deg,#27327a 0%,#232d6c 60%,#1e2760 100%);clip-path:polygon(0 0,100% 0,100% 678px,50% 802px,0 678px)}
.core-photo{left:0;top:0;width:1200px;height:802px;background:radial-gradient(ellipse at 60% 65%,rgba(120,140,200,.28) 0%,rgba(0,0,0,0) 60%)}
.core-title{left:0;top:60px;width:1200px;text-align:center}
.competency{width:230px;text-align:center;color:#fff}
.competency .icon{width:50px;height:50px;border-radius:50%;background:var(--green);margin:0 auto 10px;display:flex;align-items:center;justify-content:center}
.competency.featured .icon{background:var(--navy)}
.competency h3{font-size:18px;font-weight:600;margin-bottom:8px}
.competency p{font-size:10.5px;line-height:15.5px;color:#dfe3f2}
.competency.featured p{color:#f4f9ec}

/* services */
.services-title{left:0;top:2232px;width:1200px;text-align:center}
.service{width:196px;height:164px;border:2px solid #b9bfd6;background:#fff;display:flex;flex-direction:column;align-items:center;justify-content:center;text-align:center;padding:0 10px}
.service .icon{width:50px;height:50px;border-radius:50%;display:flex;align-items:center;justify-content:center;margin-bottom:10px}
.service .navy{background:var(--navy)}
.service .green{background:var(--green)}
.service h4{font-size:15px;line-height:21px;font-weight:600;color:var(--navy)}

/* projects */
.projects{left:0;top:2786px;width:1200px;height:662px;background:var(--mist)}
.card{width:314px;height:374px;background:#fff}
.card .thumb{width:314px;height:214px}
.card .body{padding:16px 28px}
.card h5{font-size:14.5px;line-height:23px;color:var(--navy);font-weight:600}
.card p{font-size:11.5px;line-height:17px;color:var(--muted);margin-top:8px}
.card .more{display:inline-block;margin-top:10px;font-size:10px;font-weight:600;color:var(--navy);text-decoration:underline}

/* contact */
.contact{left:0;top:3448px;width:1200px;height:640px;background:linear-gradient(180deg,#26317a 0%,#222c6b 100%)}
.contact-copy{left:156px;top:3560px;color:#fff}
.contact-item{display:flex;gap:18px;align-items:flex-start;position:absolute;left:156px;color:#fff}
.contact-item .dot{width:38px;height:38px;border-radius:50%;background:var(--green);display:flex;align-items:center;justify-content:center;flex:none}
.contact-item b{display:block;font-size:17px;font-weight:600}
.contact-item span{font-size:18px;color:#e6e9f5}
.form-panel{left:562px;top:3557px;width:566px;height:394px;background:var(--green);border-radius:60px 0 60px 0}
.form-title{left:610px;top:3600px;color:#fff;font-family:"Cinzel",serif;font-weight:600;font-size:25px;letter-spacing:1px}
.field{background:#fff;height:40px;font-size:12px;color:#555;padding:14px 20px 0}
.btn-outline{left:610px;top:3865px;width:182px;height:44px;border:2px solid #fff;color:#fff;font-size:13px;font-weight:600;display:flex;align-items:center;justify-content:center;letter-spacing:.5px}

/* footer */
.footer-divider{top:4087px;width:1px;height:319px;background:#d5d8e4}
.footer-head{font-size:18px;font-weight:600;color:var(--navy);letter-spacing:.5px;border-left:3px solid var(--green);padding-left:22px;line-height:20px}
.footer-link{font-size:15px;color:var(--navy)}
.footer-contact{display:flex;align-items:center;gap:14px;font-size:16px;color:var(--navy);position:absolute;left:855px}
.footer-contact .dot{width:30px;height:30px;border-radius:50%;background:var(--green);display:flex;align-items:center;justify-content:center}
.base-rule{left:0;top:4406px;width:1200px;height:1px;background:#d5d8e4}
.copyright{left:0;top:4436px;width:1200px;text-align:center;font-size:13px;color:var(--navy)}
</style>
</head>
<body>

<div class="abs hero" role="img" aria-label="Photo of the Nation's Capitol building under a bright sky with an American flag waving"></div>
<svg class="abs hero-band" width="1200" height="210" viewBox="0 0 1200 210" aria-hidden="true">
  <polygon points="0,40 600,185 1200,40 1200,64 600,202 0,64" fill="#ffffff"/>
  <polygon points="150,76 600,185 1050,76 1050,86 600,202 150,86" fill="#8dc63f"/>
</svg>

<div class="abs topbar-green"></div>
<div class="abs topbar-navy"></div>
<div class="abs topbar-text" style="left:588px">
  <span class="topbar-icon"><svg width="12" height="9" viewBox="0 0 12 9"><rect x=".5" y=".5" width="11" height="8" fill="none" stroke="#8dc63f"/><path d="M.5.5 6 5l5.5-4.5" fill="none" stroke="#8dc63f"/></svg></span>
  Email Us: info@keystoneridge.com
</div>
<div class="abs topbar-text" style="left:888px">
  <span class="topbar-icon"><svg width="11" height="11" viewBox="0 0 24 24"><path d="M6.6 10.8a15 15 0 0 0 6.6 6.6l2.2-2.2c.3-.3.7-.4 1-.2 1.1.4 2.3.6 3.6.6.6 0 1 .4 1 1V20c0 .6-.4 1-1 1A17 17 0 0 1 3 4c0-.6.4-1 1-1h3.5c.6 0 1 .4 1 1 0 1.3.2 2.5.6 3.6.1.3 0 .7-.2 1z" fill="#24306e"/></svg></span>
  CALL US: 555.214.6093
</div>

<div class="abs logo">
  <div class="logo-mark"></div>
  <div class="logo-name">KEYSTONE RIDGE</div>
  <div class="logo-sub">CONSTRUCTION, LLC</div>
</div>

<nav class="abs nav">
  <a class="active" style="left:399px">HOME</a>
  <span class="sep" style="left:468px"></span>
  <a style="left:494px">ABOUT US</a>
  <span class="sep" style="left:592px"></span>
  <a style="left:620px">SERVICES</a>
  <span class="sep" style="left:716px"></span>
  <a style="left:748px">WHY US</a>
  <span class="sep" style="left:830px"></span>
  <a style="left:858px">PROJECTS</a>
  <span class="sep" style="left:960px"></span>
  <a style="left:988px">CONTACT</a>
</nav>

<div class="abs hero-tag">KEYSTONE RIDGE CONSTRUCTION</div>
<h1 class="abs hero-title">VETERAN OWNED BUILDING<br>CONSTRUCTION COMPANY</h1>
<div class="abs btn-navy">LEARN MORE</div>
<svg class="abs hero-arrow" style="left:40px" width="24" height="44" viewBox="0 0 24 44"><path d="M22 2 3 22l19 20" fill="none" stroke="#24306e" stroke-width="3"/></svg>
<svg class="abs hero-arrow" style="left:1122px" width="24" height="44" viewBox="0 0 24 44"><path d="M2 2l19 20L2 42" fill="none" stroke="#24306e" stroke-width="3"/></svg>

<div class="abs about-frame"></div>
<div class="abs about-green-left"></div>
<div class="abs about-green-right"></div>
<div class="abs about-photo" role="img" aria-label="Photo of a modern white multi-storey federal office building with landscaped grounds"></div>
<div class="abs about-copy">
  <div class="eyebrow">WHO WE ARE</div>
  <h2 class="heading" style="margin-top:6px">ABOUT KEYSTONE RIDGE<br>CONSTRUCTION</h2>
  <p>Keystone Ridge Construction, LLC is a veteran-owned business, and is a leading force in the construction industry. We have continuously provided exceptional services to our clients. With a wealth of experience and a commitment of excellence, we have earned a reputation for delivering high-quality projects on time and within budget.</p>
  <div class="btn-green" style="margin-top:36px">LEARN MORE</div>
</div>

<section class="abs core">
  <div class="abs core-photo" role="img" aria-label="Faded photo of the Capitol building behind the section"></div>
  <div class="abs core-title">
    <div class="eyebrow">WHY CHOOSE US</div>
    <h2 class="heading" style="color:#fff;margin-top:6px">CORE COMPETENCIES</h2>
    <div class="rule" style="margin:14px auto 0"></div>
  </div>
  <svg class="abs" style="left:0;top:0" width="1200" height="802" viewBox="0 0 1200 802" aria-hidden="true">
    <g fill="none" stroke="#8e97c4" stroke-width="1.2">
      <polygon points="240,175 410,345 240,515 70,345"/>
      <polygon points="951,175 1121,345 951,515 781,345"/>
      <polygon points="417,377 587,547 417,717 247,547"/>
      <polygon points="773,377 943,547 773,717 603,547"/>
    </g>
    <polygon points="596,175 766,345 596,515 426,345" fill="#8dc63f"/>
  </svg>

  <div class="abs competency" style="left:125px;top:230px">
    <div class="icon"><svg width="26" height="26" viewBox="0 0 26 26"><g fill="none" stroke="#fff" stroke-width="1.6"><circle cx="8" cy="8" r="3"/><circle cx="18" cy="8" r="3"/><path d="M3 20c0-4 2-6 5-6s5 2 5 6M13 20c0-4 2-6 5-6s5 2 5 6"/></g></svg></div>
    <h3>Experience</h3>
    <p>With decades of experience, we bring unparalleled expertise to every project we undertake. Our team consists of seasoned professionals who are experts in their respective fields.</p>
  </div>
  <div class="abs competency featured" style="left:481px;top:230px">
    <div class="icon"><svg width="26" height="26" viewBox="0 0 26 26"><g fill="none" stroke="#fff" stroke-width="1.6"><path d="M13 3l8 3v6c0 5-4 9-8 11-4-2-8-6-8-11V6z"/><path d="M9 13l3 3 5-6"/></g></svg></div>
    <h3>Safety</h3>
    <p>Safety is our top priority on every job site. We adhere to the highest safety standards and implement rigorous safety protocols to ensure the well-being of our workers and stakeholders.</p>
  </div>
  <div class="abs competency" style="left:836px;top:230px">
    <div class="icon"><svg width="26" height="26" viewBox="0 0 26 26"><g fill="none" stroke="#fff" stroke-width="1.6"><circle cx="13" cy="13" r="10"/><path d="M7 14l4 3 8-7"/></g></svg></div>
    <h3>Client Satisfaction</h3>
    <p>Our commitment to client satisfaction is unwavering. We prioritize open communication, transparency, and responsiveness, working closely with clients to understand their needs and deliver results.</p>
  </div>
  <div class="abs competency" style="left:302px;top:450px">
    <div class="icon"><svg width="26" height="26" viewBox="0 0 26 26"><g fill="none" stroke="#fff" stroke-width="1.6"><rect x="5" y="6" width="10" height="16"/><rect x="15" y="11" width="6" height="11"/><path d="M8 10h4M8 14h4M8 18h4"/></g></svg></div>
    <h3>Portfolio</h3>
    <p>Our portfolio encompasses a wide range of construction projects, including commercial building, industrial facilities, infrastructure development and more.</p>
  </div>
  <div class="abs competency" style="left:658px;top:450px">
    <div class="icon"><svg width="26" height="26" viewBox="0 0 26 26"><g fill="none" stroke="#fff" stroke-width="1.6"><path d="M13 4a6 6 0 0 0-3.5 11v3h7v-3A6 6 0 0 0 13 4z"/><path d="M10 21h6"/></g></svg></div>
    <h3>Innovation</h3>
    <p>We stay at the forefront of industry trends and technologies, leveraging the latest tools and techniques to deliver innovative solutions.</p>
  </div>
</section>

<div class="abs services-title">
  <div class="eyebrow">WHAT WE DO</div>
  <h2 class="heading" style="margin-top:6px">KEY SERVICES</h2>
  <div class="rule" style="margin:14px auto 0"></div>
</div>

<div class="abs service" style="left:86px;top:2351px"><span class="icon navy"><svg width="24" height="24" viewBox="0 0 24 24"><g fill="none" stroke="#fff" stroke-width="1.6"><path d="M4 20h16M6 20V9l6-4 6 4v11M10 20v-5h4v5"/></g></svg></span><h4>General<br>Contracting</h4></div>
<div class="abs service" style="left:292px;top:2351px"><span class="icon green"><svg width="24" height="24" viewBox="0 0 24 24"><g fill="none" stroke="#fff" stroke-width="1.6"><path d="M5 21V5h8v16M13 10h6v11M3 21h18M8 9h2M8 13h2M8 17h2"/></g></svg></span><h4>Construction<br>Management</h4></div>
<div class="abs service" style="left:498px;top:2351px"><span class="icon navy"><svg width="24" height="24" viewBox="0 0 24 24"><g fill="none" stroke="#fff" stroke-width="1.6"><rect x="4" y="4" width="16" height="16"/><path d="M4 10h16M10 10v10"/></g></svg></span><h4>Design-Build<br>Services</h4></div>
<div class="abs service" style="left:704px;top:2351px"><span class="icon green"><svg width="24" height="24" viewBox="0 0 24 24"><g fill="none" stroke="#fff" stroke-width="1.6"><circle cx="12" cy="12" r="4"/><path d="M12 3v3M12 18v3M3 12h3M18 12h3M5.6 5.6l2 2M16.4 16.4l2 2M5.6 18.4l2-2M16.4 7.6l2-2"/></g></svg></span><h4>Pre-construction<br>Planning</h4></div>
<div class="abs service" style="left:910px;top:2351px"><span class="icon navy"><svg width="24" height="24" viewBox="0 0 24 24"><g fill="none" stroke="#fff" stroke-width="1.6"><path d="M4 15a8 8 0 0 1 16 0zM3 15h18v3H3zM12 7V4"/></g></svg></span><h4>Sustainable<br>Construction<br>Practices</h4></div>

<div class="abs service" style="left:86px;top:2528px"><span class="icon green"><svg width="24" height="24" viewBox="0 0 24 24"><g fill="none" stroke="#fff" stroke-width="1.6"><circle cx="12" cy="8" r="4"/><path d="M5 21c0-4 3-7 7-7s7 3 7 7"/></g></svg></span><h4>Value<br>Engineering</h4></div>
<div class="abs service" style="left:292px;top:2528px"><span class="icon navy"><svg width="24" height="24" viewBox="0 0 24 24"><g fill="none" stroke="#fff" stroke-width="1.6"><path d="M14 4l6 6-10 10H4v-6z"/><path d="M12 6l6 6"/></g></svg></span><h4>Renovation and<br>Remodeling</h4></div>
<div class="abs service" style="left:498px;top:2528px"><span class="icon green"><svg width="24" height="24" viewBox="0 0 24 24"><g fill="none" stroke="#fff" stroke-width="1.6"><circle cx="10" cy="10" r="6"/><path d="M14.5 14.5 20 20M7.5 10l2 2 3.5-4"/></g></svg></span><h4>Quality Assurance<br>and Control</h4></div>
<div class="abs service" style="left:704px;top:2528px"><span class="icon navy"><svg width="24" height="24" viewBox="0 0 24 24"><g fill="none" stroke="#fff" stroke-width="1.6"><rect x="5" y="3" width="14" height="18"/><path d="M8 7h8M8 11h2M12 11h2M8 15h2M12 15h2M16 11v6"/></g></svg></span><h4>Project Estimating<br>and Budgeting</h4></div>
<div class="abs service" style="left:910px;top:2528px"><span class="icon green"><svg width="24" height="24" viewBox="0 0 24 24"><g fill="none" stroke="#fff" stroke-width="1.6"><path d="M6 3h9l4 4v14H6z"/><path d="M9 10h7M9 14h7M9 18h4"/></g></svg></span><h4>Permitting and<br>Regulatory<br>Compliance</h4></div>

<section class="abs projects">
  <div class="abs" style="left:130px;top:70px">
    <div class="eyebrow">OUR PROJECTS</div>
    <h2 class="heading" style="margin-top:4px">RECENT PROJECTS</h2>
  </div>
  <article class="abs card" style="left:126px;top:192px">
    <div class="thumb" role="img" aria-label="Photo of a glass-fronted federal office building surrounded by trees" style="background:linear-gradient(180deg,#6fa4d8 0%,#4f7fb3 55%,#4f7d3a 100%)"></div>
    <div class="body"><h5>Lorem ipsum dolor sit amet con-<br>sectetur adipiscing elit</h5><p>Lorem ipsum dolor sit amet, consectetur adipiscing elit sed do eiusmod</p><span class="more">LEARN MORE</span></div>
  </article>
  <article class="abs card" style="left:466px;top:192px">
    <div class="thumb" role="img" aria-label="Photo of a bright office interior corridor with plants and desks" style="background:linear-gradient(180deg,#e9ece9 0%,#d4d8d2 55%,#9aa898 100%)"></div>
    <div class="body"><h5>Lorem ipsum dolor sit amet con-<br>sectetur adipiscing elit</h5><p>Lorem ipsum dolor sit amet, consectetur adipiscing elit sed do eiusmod</p><span class="more">LEARN MORE</span></div>
  </article>
  <article class="abs card" style="left:808px;top:192px">
    <div class="thumb" role="img" aria-label="Photo of an interior room under renovation with a ladder and bare walls" style="background:linear-gradient(90deg,#b89570 0%,#d6c0a2 50%,#e5e0da 100%)"></div>
    <div class="body"><h5>Lorem ipsum dolor sit amet con-<br>sectetur adipiscing elit</h5><p>Lorem ipsum dolor sit amet, consectetur adipiscing elit sed do eiusmod</p><span class="more">LEARN MORE</span></div>
  </article>
</section>

<section class="abs contact"></section>
<div class="abs contact-copy">
  <div class="eyebrow">GET IN TOUCH</div>
  <h2 class="heading" style="color:#fff;margin-top:4px">CONTACT US</h2>
  <div class="rule" style="margin-top:10px"></div>
  <div style="font-size:18px;font-weight:600;margin-top:34px">Douglas Whitfield, President</div>
</div>
<div class="contact-item" style="top:3740px">
  <span class="dot"><svg width="18" height="13" viewBox="0 0 18 13"><rect x="1" y="1" width="16" height="11" fill="none" stroke="#fff" stroke-width="1.5"/><path d="M1 1l8 6 8-6" fill="none" stroke="#fff" stroke-width="1.5"/></svg></span>
  <div><b>Email address</b><span>info@keystoneridge.com</span></div>
</div>
<div class="contact-item" style="top:3822px">
  <span class="dot"><svg width="18" height="18" viewBox="0 0 18 18"><g fill="none" stroke="#fff" stroke-width="1.5"><circle cx="9" cy="9" r="7.5"/><path d="M1.5 9h15M9 1.5c3 3 3 12 0 15M9 1.5c-3 3-3 12 0 15"/></g></svg></span>
  <div><b>Website</b><span>www.keystoneridge.com</span></div>
</div>
<div class="contact-item" style="top:3902px">
  <span class="dot"><svg width="16" height="16" viewBox="0 0 24 24"><path d="M6.6 10.8a15 15 0 0 0 6.6 6.6l2.2-2.2c.3-.3.7-.4 1-.2 1.1.4 2.3.6 3.6.6.6 0 1 .4 1 1V20c0 .6-.4 1-1 1A17 17 0 0 1 3 4c0-.6.4-1 1-1h3.5c.6 0 1 .4 1 1 0 1.3.2 2.5.6 3.6.1.3 0 .7-.2 1z" fill="#fff"/></svg></span>
  <div><b>Phone Number</b><span>555.214.6093</span></div>
</div>

<div class="abs form-panel"></div>
<div class="abs form-title">LEAVE US A MESSAGE</div>
<div class="abs field" style="left:610px;top:3648px;width:232px">First Name</div>
<div class="abs field" style="left:850px;top:3648px;width:233px">Last Name</div>
<div class="abs field" style="left:610px;top:3704px;width:232px">Email address</div>
<div class="abs field" style="left:850px;top:3704px;width:233px">Phone Number</div>
<div class="abs field" style="left:610px;top:3760px;width:473px;height:88px">Message</div>
<div class="abs btn-outline">SEND MESSAGE</div>

<div class="abs footer-divider" style="left:452px"></div>
<div class="abs footer-divider" style="left:830px"></div>
<div class="abs logo" style="left:150px;top:4180px;width:226px">
  <div class="logo-mark"></div>
  <div class="logo-name">KEYSTONE RIDGE</div>
  <div class="logo-sub">CONSTRUCTION, LLC</div>
</div>

<div class="abs footer-head" style="left:475px;top:4160px">NAVIGATION</div>
<span class="abs footer-link" style="left:480px;top:4205px">About Us</span>
<span class="abs footer-link" style="left:480px;top:4240px">Services</span>
<span class="abs footer-link" style="left:480px;top:4275px">Why Us</span>
<span class="abs footer-link" style="left:480px;top:4310px">Contact us</span>
<span class="abs footer-link" style="left:638px;top:4205px">Projects</span>
<span class="abs footer-link" style="left:638px;top:4240px">Blogs</span>
<span class="abs footer-link" style="left:638px;top:4275px">Terms of Use</span>
<span class="abs footer-link" style="left:638px;top:4310px">Privacy Policy</span>

<div class="abs footer-head" style="left:832px;top:4160px">CONTACT US</div>
<div class="footer-contact" style="top:4208px"><span class="dot"><svg width="14" height="10" viewBox="0 0 18 13"><rect x="1" y="1" width="16" height="11" fill="none" stroke="#fff" stroke-width="1.8"/><path d="M1 1l8 6 8-6" fill="none" stroke="#fff" stroke-width="1.8"/></svg></span>info@keystoneridge.com</div>
<div class="footer-contact" style="top:4262px"><span class="dot"><svg width="14" height="14" viewBox="0 0 18 18"><g fill="none" stroke="#fff" stroke-width="1.8"><circle cx="9" cy="9" r="7.5"/><path d="M1.5 9h15M9 1.5c3 3 3 12 0 15M9 1.5c-3 3-3 12 0 15"/></g></svg></span>www.keystoneridge.com</div>
<div class="footer-contact" style="top:4316px"><span class="dot"><svg width="13" height="13" viewBox="0 0 24 24"><path d="M6.6 10.8a15 15 0 0 0 6.6 6.6l2.2-2.2c.3-.3.7-.4 1-.2 1.1.4 2.3.6 3.6.6.6 0 1 .4 1 1V20c0 .6-.4 1-1 1A17 17 0 0 1 3 4c0-.6.4-1 1-1h3.5c.6 0 1 .4 1 1 0 1.3.2 2.5.6 3.6.1.3 0 .7-.2 1z" fill="#fff"/></svg></span>555.214.6093</div>

<div class="abs base-rule"></div>
<div class="abs copyright">Copyright © 2024 Keystone Ridge. All Right Reserved</div>

</body>
</html>
```